HR Company Website

Home page and information page needs for Human resources company
SERVICES

Employment Law - -
HR Advice -
Recruitment -
Disciplinaries -
Redundancies -
Coaching & Training -
HR Policy Review -
Contract Writing -
Tribunal Claims -
HR Partner -

LAYOUT SKETCH DISCUSSED:
Yes
On the animation the left hand side messgae banner will be constant along with the button , the right hand side will be animated.

COMPETITION
Grove HR - www.grovehr-example.com
Ky HR - www.kyhr-example.co.uk
Tern HR - www.ternhr-example.com

COMPANY LOGO
Client currently has no logo - Bolvinex to design

STRAPLINE:
Tern HR Partner

ACCREDITATIONS / LOGOS:
Masters Diploma in Emloyment Law

WEBSITE THEME:
Human Resources

MAIN BODY OF WEBSITE:
Light

IMAGES THAT BEST REFLECT YOUR COMPANY:
Staff / Office Based Life style images People groups - no face close ups
planning
infrastructure
NOTHING TOO OBVIOUS

PAGES:

Home
About Us
Our Services
- Employment Law Advice
- HR Advice
- Contracts of Employment
- HR Policies
- Disciplinary Procedures
- Redundancy Advice
Contact Us

MESSAGE BANNERS:
1. 12 Years HR Experience - wealth of experience & knowledge
2. Cost Effective Solution - use us when you need us
3. Personal HR Approach - create bespoke tailored made solutions
4. Preventative Measures Protects - don't leave it until is is too late
5. Complete Peace of Mind - Let us be Tern HR department

Target Market(s)

Male & Femaie - 30-60

SME Business

Industry/Entity Type

Consulting

Number of Pages Required

2 pages

Requirements
Must have
• This design will be built using the wordpress platform, use the wireframe attached for the layout structure - must be visually impactful - clean and proefessional looking
Nice to have
• I have attached the logo - do not amend the colout but you can add effects onto it if you wish to
Should not have
• Loads of text

```html
<!DOCTYPE html>
<html lang="en">
<head>
<meta charset="utf-8">
<title>Meridel HR Ltd – Tern HR Partner</title>
<link href="https://fonts.googleapis.com/css2?family=Noto+Sans:ital,wght@0,400;0,700;1,400;1,700&family=Arimo:wght@400&display=swap" rel="stylesheet">
<style>
:root{
  --green-dark:#0a6a2e;
  --green-mid:#2f9a3c;
  --green-light:#63b83a;
  --brand-green:#0f7a35;
  --lime:#8cc63f;
  --footer-bg:#0f3a1d;
  --footer-deep:#082a14;
  --text-grey:#6b6b6b;
  --nav-text:#123a1e;
}
*{box-sizing:border-box;margin:0;padding:0}
html,body{width:1200px;height:1132px;overflow:hidden;background:#fff}
body{font-family:"Noto Sans",sans-serif;position:relative}

.site-header{position:absolute;left:0;top:0;width:1200px;height:95px;background:linear-gradient(#fff,#ececec);border-bottom:1px solid #cfcfcf}
.brand{position:absolute;left:110px;top:14px;display:flex;align-items:center;gap:10px}
.brand-mark{width:14px;height:14px;background:var(--brand-green)}
.brand-name{font-size:36px;font-weight:400;color:var(--brand-green);line-height:1}
.brand-tagline{position:absolute;left:196px;top:68px;font-size:15px;font-style:italic;color:var(--lime)}
.header-phone{position:absolute;right:110px;top:12px;font-size:16px;color:#666;display:flex;align-items:center;gap:6px}
.header-phone strong{color:var(--brand-green);font-weight:400;letter-spacing:.5px}
.main-nav{position:absolute;right:110px;top:50px;display:flex}
.main-nav a{font-size:16px;font-weight:700;color:var(--nav-text);text-decoration:none;padding:9px 24px;letter-spacing:.3px}
.main-nav a.current{background:linear-gradient(#e4e4e4,#cfcfcf);color:#666;border-radius:4px 4px 0 0;margin-right:2px}

.hero{position:absolute;left:0;top:95px;width:1200px;height:352px;background:linear-gradient(100deg,#4fae35 0%,#3a9d3a 35%,#25893a 70%,#1c7a34 100%);overflow:hidden}
.hero-photo{position:absolute;left:620px;top:0;width:500px;height:352px;background:linear-gradient(90deg,rgba(120,190,120,0) 0%,rgba(190,215,190,.55) 35%,rgba(210,200,190,.7) 65%,rgba(60,140,70,.4) 100%)}
.hero-title{position:absolute;left:100px;top:74px;font-size:50px;line-height:62px;color:#fff;font-weight:400;letter-spacing:.5px}
.hero-title em{font-style:italic}
.audit-button{position:absolute;left:299px;top:217px;width:234px;height:53px;border-radius:27px;background:linear-gradient(#7a7a7a,#4a4a4a);color:#ddd;font-size:21px;font-weight:700;text-align:center;line-height:53px;letter-spacing:.5px;box-shadow:0 2px 4px rgba(0,0,0,.35)}
.hero-quote{position:absolute;left:635px;top:148px;font-size:21px;line-height:25px;color:#fff}
.hero-quote b{font-weight:700}
.hero-dots{position:absolute;left:570px;top:325px;display:flex;gap:7px}
.hero-dots span{width:13px;height:13px;border-radius:50%;background:#0b5a25}
.hero-rule{position:absolute;left:0;top:447px;width:1200px;height:3px;background:#1d5a2c}

.feature{position:absolute;top:480px;width:330px}
.feature-title{font-size:20px;color:#143a1e;display:flex;align-items:center;gap:10px;margin-left:-38px}
.feature-title svg{flex:none}
.feature-text{margin-top:8px;font-family:"Arimo",sans-serif;font-size:12.5px;line-height:17.7px;color:var(--text-grey);width:238px}
.read-more{display:inline-block;margin-top:8px;width:126px;height:25px;border-radius:13px;background:linear-gradient(#8c8c8c,#555);color:#fff;font-size:13px;text-align:center;line-height:25px;box-shadow:0 2px 3px rgba(0,0,0,.3)}
.feature-law{left:148px}
.feature-approach{left:503px}
.feature-rates{left:867px}
.feature-rates .feature-text{width:235px}

.testimonial{position:absolute;left:100px;top:700px;width:1000px;height:62px;border:1px dotted #bbb;background:#fafafa;text-align:center;font-size:22px;line-height:60px;font-style:italic;color:var(--brand-green);letter-spacing:.2px}

.site-footer{position:absolute;left:0;top:804px;width:1200px;height:328px;background:radial-gradient(ellipse at 50% 30%,#174a26,var(--footer-bg) 55%,var(--footer-deep))}
.footer-col{position:absolute;top:0}
.footer-divider{position:absolute;top:0;width:1px;height:328px;background:rgba(0,0,0,.35);box-shadow:1px 0 0 rgba(255,255,255,.05)}
.footer-heading{font-size:19px;font-weight:700;color:#fff;line-height:22px}
.footer-heading em{font-weight:400}
.address{margin-top:24px;font-family:"Arimo",sans-serif;font-size:12.5px;line-height:17.7px;color:#ddd;font-style:normal}
.address u{color:#fff}
.call-col{left:477px;width:330px;height:328px}
.call-text{position:relative;z-index:1;margin-top:36px}
.call-lead{font-size:31px;line-height:36px;color:#bbb;font-weight:700;margin-top:26px;width:170px}
.call-sub{font-size:16px;font-weight:700;color:#8aa28f;line-height:18px;margin-top:-2px}
.handset{position:absolute;left:178px;top:22px;width:125px;height:215px;border-radius:18px;background:linear-gradient(135deg,#3a3a3a,#1a2a1e)}
.contact-form{margin-top:12px;width:228px}
.field{height:24px;margin-bottom:4px;background:#444;border:1px solid #666;font-family:"Arimo",sans-serif;font-size:11px;color:#ddd;padding:4px 10px}
.field-comments{height:72px}
.submit{margin-top:2px;width:92px;height:24px;border-radius:12px;background:linear-gradient(#999,#555);color:#fff;font-size:13px;font-weight:700;text-align:center;line-height:24px}
</style>
</head>
<body>

<header class="site-header">
  <div class="brand"><span class="brand-mark"></span><span class="brand-name">Meridel HR Ltd</span></div>
  <div class="brand-tagline">Tern HR Partner</div>
  <div class="header-phone">
    <svg width="13" height="13" viewBox="0 0 13 13"><rect width="13" height="13" rx="2" fill="#2f9a3c"/><path d="M4 3l2 2-1 1c.5 1 1 1.5 2 2l1-1 2 2-1.2 1.2C6 10 3 7 2.8 4.2z" fill="#fff"/></svg>
    Call us today! <strong>(555) 010 2030</strong>
  </div>
  <nav class="main-nav">
    <a class="current">HOME</a><a>ABOUT US</a><a>OUR SERVICES</a><a>CONTACT US</a>
  </nav>
</header>

<section class="hero">
  <div class="hero-photo" role="img" aria-label="Smiling businessman in a grey suit in a bright office"></div>
  <h1 class="hero-title">Is <em>your</em> company<br>legally compliant</h1>
  <div class="audit-button">FREE HR AUDIT</div>
  <p class="hero-quote">"Over <b><i>12 years</i></b> HR<br>experience - a wealth of<br><b>knowledge</b>"</p>
  <div class="hero-dots"><span></span><span></span><span></span></div>
</section>
<div class="hero-rule"></div>

<article class="feature feature-law">
  <h2 class="feature-title"><svg width="28" height="26" viewBox="0 0 28 26"><path d="M3 16l8-9 5 3 8-7 2 3-9 9-5-3-6 7z" fill="#2f9a3c"/><rect x="1" y="15" width="6" height="9" fill="#555" transform="rotate(-40 4 19)"/></svg>Employment Law Advice</h2>
  <p class="feature-text">Lorem ipsum dolor sit amet, consectetur adipiscing elit. Nam semper est in libero tristique viverra vitae in nunc. Sed odio tortor, elementum quis eleifend ac, viverra ut magna. Vivamus odio diam, aliquet et pharetra quis, laoreet id urna. Nullam vel nisl mauris.fames ac turpis egestas.</p>
  <span class="read-more">READ MORE</span>
</article>
<article class="feature feature-approach">
  <h2 class="feature-title"><svg width="24" height="28" viewBox="0 0 24 28"><circle cx="12" cy="7" r="5" fill="#666"/><path d="M2 27v-8c0-4 4-6 10-6s10 2 10 6v8z" fill="#555"/><path d="M11 14h2l1 8-2 2-2-2z" fill="#2f9a3c"/></svg>Personal HR Approach</h2>
  <p class="feature-text">Lorem ipsum dolor sit amet, consectetur adipiscing elit. Nam semper est in libero tristique viverra vitae in nunc. Sed odio tortor, elementum quis eleifend ac, viverra ut magna. Vivamus odio diam, aliquet et pharetra quis, laoreet id urna. Nullam vel nisl mauris.fames ac turpis egestas.</p>
  <span class="read-more">READ MORE</span>
</article>
<article class="feature feature-rates">
  <h2 class="feature-title"><svg width="26" height="28" viewBox="0 0 26 28"><rect x="4" y="1" width="20" height="25" rx="2" fill="#fff" stroke="#555" stroke-width="1.5"/><path d="M9 7h11M9 11h11M9 15h8" stroke="#777" stroke-width="1.5"/><path d="M1 20l4 5 7-10" fill="none" stroke="#2f9a3c" stroke-width="2.5"/></svg>Rates &amp; Packages</h2>
  <p class="feature-text">Lorem ipsum dolor sit amet, consectetur adipiscing elit. Nam semper est in libero tristique viverra vitae in nunc. Sed odio tortor, elementum quis eleifend ac, viverra ut magna. Vivamus odio diam, aliquet et pharetra quis, laoreet id urna. Nullam vel nisl mauris.fames ac turpis egestas.</p>
  <span class="read-more">READ MORE</span>
</article>

<blockquote class="testimonial">"Testimonial goes here - a very pleased client - testimonial goes here - a very pleased client - "</blockquote>

<footer class="site-footer">
  <div class="footer-col" style="left:110px;top:36px">
    <h3 class="footer-heading">Meridel HR Ltd: <em><i>Tern HR Partner</i></em></h3>
    <address class="address">Building No. #545<br>Street No #<br>City, State 10000<br>United States<br>Fax: (555) 010 2031<br>Phone: (555) 010 2030<br>Email: <u>info@meridelhr-example.com</u></address>
  </div>
  <div class="footer-divider" style="left:423px"></div>
  <div class="footer-col call-col">
    <div class="handset" role="img" aria-label="Black telephone handset with coiled cord"></div>
    <div class="call-text">
      <h3 class="footer-heading">Is your company<br>breaking the law?</h3>
      <p class="call-lead">Call Us to Today</p>
      <p class="call-sub">And let us protect<br>your business</p>
    </div>
  </div>
  <div class="footer-divider" style="left:826px"></div>
  <div class="footer-col" style="left:871px;top:36px">
    <h3 class="footer-heading">Find out now if your<br>business protected</h3>
    <form class="contact-form">
      <div class="field">Name:</div>
      <div class="field">Email:</div>
      <div class="field">Telephone:</div>
      <div class="field field-comments">Comments:</div>
      <div class="submit">SUBMIT</div>
    </form>
  </div>
</footer>

</body>
</html>
```